We are looking to create a graphic that will be used in Facebook posts each week to show the daily Porchlight Report. Attached is an example of what we are looking for. We need to be able to update the forecast. So we will need hi-res vector files. The graphics need to represent the level of mosquito activity: SLIGHT, AVERAGE, INTENSE, EXTREME

```html
<!DOCTYPE html>
<html lang="en">
<head>
<meta charset="utf-8">
<title>Porchlight Report – Activity Levels</title>
<link rel="stylesheet" href="https://fonts.googleapis.com/css2?family=Montserrat:wght@700&display=swap">
<style>
  :root {
    --bg: #ffffff;
    --track: #d7d7d7;
    --ink: #111111;
    --green-light: #b7d55c;
    --green-dark: #5aaf2e;
    --orange: #f5a100;
    --orange-soft: #dcb83c;
    --orange-deep: #f08a00;
    --red: #e30613;
    --red-deep: #c80d12;
    --maroon: #5a0c05;
  }
  html, body {
    margin: 0;
    padding: 0;
    width: 1200px;
    height: 494px;
    overflow: hidden;
    background: var(--bg);
  }
  .activity-scale {
    position: relative;
    width: 1200px;
    height: 494px;
  }
  .gauges {
    position: absolute;
    left: 0;
    top: 0;
  }
  .track { fill: none; stroke: var(--track); stroke-width: 35; }
  .segment { fill: none; stroke-width: 35; stroke-linecap: butt; }
  .level-label {
    position: absolute;
    top: 366px;
    width: 240px;
    margin-left: -120px;
    text-align: center;
    font-family: "Montserrat", sans-serif;
    font-weight: 700;
    font-size: 34px;
    letter-spacing: 0.03em;
    color: var(--ink);
    line-height: 44px;
  }
</style>
</head>
<body>
<main class="activity-scale">
  <svg class="gauges" width="1200" height="494" viewBox="0 0 1200 494">
    <defs>
      <linearGradient id="grad-green" x1="0" y1="0" x2="1" y2="0">
        <stop offset="0" stop-color="var(--green-light)"/>
        <stop offset="1" stop-color="var(--green-dark)"/>
      </linearGradient>
      <linearGradient id="grad-orange" x1="0" y1="0" x2="0" y2="1">
        <stop offset="0" stop-color="var(--orange)"/>
        <stop offset="0.75" stop-color="var(--orange)"/>
        <stop offset="1" stop-color="var(--orange-soft)"/>
      </linearGradient>
      <linearGradient id="grad-hot" x1="0" y1="0" x2="1" y2="0">
        <stop offset="0" stop-color="var(--orange-deep)"/>
        <stop offset="1" stop-color="var(--red)"/>
      </linearGradient>
      <linearGradient id="grad-burn" x1="1" y1="0" x2="0" y2="1">
        <stop offset="0" stop-color="var(--red-deep)"/>
        <stop offset="1" stop-color="var(--maroon)"/>
      </linearGradient>
    </defs>

    <!-- Slight -->
    <g class="gauge gauge-slight">
      <circle class="track" cx="173" cy="201" r="115"/>
      <path class="segment" stroke="url(#grad-green)" d="M173 316 A115 115 0 0 1 58 201"/>
      <circle cx="58" cy="201" r="17.5" fill="var(--green-light)"/>
      <rect x="109" y="148" width="137" height="117" rx="14" fill="var(--green-dark)" role="img" aria-label="Mosquito silhouette in green"/>
    </g>

    <!-- Average -->
    <g class="gauge gauge-average">
      <circle class="track" cx="461" cy="201" r="115"/>
      <path class="segment" stroke="url(#grad-green)" d="M461 316 A115 115 0 0 1 346 201"/>
      <path class="segment" stroke="url(#grad-orange)" d="M346 201 A115 115 0 0 1 484.9 88.5"/>
      <circle cx="484.9" cy="88.5" r="17.5" fill="var(--orange)"/>
      <rect x="397" y="148" width="137" height="117" rx="14" fill="var(--orange)" role="img" aria-label="Mosquito silhouette in orange"/>
    </g>

    <!-- Intense -->
    <g class="gauge gauge-intense">
      <circle class="track" cx="749" cy="201" r="115"/>
      <path class="segment" stroke="url(#grad-green)" d="M749 316 A115 115 0 0 1 634 201"/>
      <path class="segment" stroke="url(#grad-orange)" d="M634 201 A115 115 0 0 1 749 86"/>
      <path class="segment" stroke="url(#grad-hot)" d="M749 86 A115 115 0 0 1 864 201"/>
      <path class="segment" stroke="var(--red)" d="M864 201 A115 115 0 0 1 862.9 217"/>
      <circle cx="862.9" cy="217" r="17.5" fill="var(--red)"/>
      <rect x="685" y="148" width="137" height="117" rx="14" fill="var(--red)" role="img" aria-label="Mosquito silhouette in red"/>
    </g>

    <!-- Extreme -->
    <g class="gauge gauge-extreme">
      <circle class="track" cx="1025" cy="201" r="115"/>
      <path class="segment" stroke="url(#grad-green)" d="M1025 316 A115 115 0 0 1 910 201"/>
      <path class="segment" stroke="url(#grad-orange)" d="M910 201 A115 115 0 0 1 1025 86"/>
      <path class="segment" stroke="url(#grad-hot)" d="M1025 86 A115 115 0 0 1 1140 201"/>
      <path class="segment" stroke="url(#grad-burn)" d="M1140 201 A115 115 0 0 1 1025 316"/>
      <circle cx="1025" cy="316" r="17.5" fill="var(--maroon)"/>
      <rect x="961" y="148" width="137" height="117" rx="14" fill="var(--maroon)" role="img" aria-label="Mosquito silhouette in dark maroon"/>
    </g>
  </svg>

  <div class="level-label" style="left:173px">SLIGHT</div>
  <div class="level-label" style="left:454px">AVERAGE</div>
  <div class="level-label" style="left:744px">INTENSE</div>
  <div class="level-label" style="left:1036px">EXTREME</div>
</main>
</body>
</html>
```